Web design - holistic filmmaker

I need a design for my new website.

I am a holistic filmmaker, ie I make films for healers, alternative practitioners, spiritual people and institutions that offer training in this field.

The design should be noble, bright, convey the feeling of space and expanse and have some particularly beautiful color accents.

The structure is: start page, offer, references, about me, imprint.

As an idea for the start page, I thought that either I could introduce myself as a filmmaker and my offer, or we could start right on the start page with the references, ie photos and links to already realized projects.

If you want more information or an exchange, I'd love to hear from you. At the moment I just don't know how to describe it better.

The winner will then be asked to design a logo.

Target Market(s)

healers, alternative practitioners, spiritual people and institutions that offer training in this field

Industry/Entity Type

Film production

Number of Pages Required

3 page

```html
<!DOCTYPE html>
<html lang="en">
<head>
<meta charset="utf-8">
<title>Jonas – Holistic Filmmaker</title>
<link href="https://fonts.googleapis.com/css2?family=Cinzel:wght@400;700&family=Oswald:wght@600&family=Roboto:wght@400;500&display=swap" rel="stylesheet">
<style>
:root{
  --bg:#1c1c1c;
  --bg-dark:#131313;
  --bg-mid:#262626;
  --gold:#cfa862;
  --gold-btn:#d4ac66;
  --white:#ffffff;
  --muted:#cfcfcf;
  --red:#e0231b;
}
*{margin:0;padding:0;box-sizing:border-box}
html,body{width:1200px;height:5272px;overflow:hidden}
body{background:var(--bg);color:var(--white);font-family:"Roboto",Arial,sans-serif;position:relative}
.serif{font-family:"Cinzel",Georgia,serif}
.gold{color:var(--gold)}
section,header,footer{position:absolute;left:0;width:1200px;overflow:hidden}
.abs{position:absolute}
.photo{position:absolute}
.btn{position:absolute;background:var(--gold-btn);color:#fff;font-size:15px;display:flex;align-items:center;justify-content:center;text-transform:uppercase;letter-spacing:.5px}
.ghost{position:absolute;font-family:"Oswald",Impact,sans-serif;font-weight:600;font-size:150px;letter-spacing:4px;color:rgba(255,255,255,.06);white-space:nowrap;left:40px}
.sec-title{position:absolute;left:0;width:1200px;text-align:center;font-family:"Cinzel",Georgia,serif;font-size:30px;letter-spacing:2px}
.kicker{position:absolute;left:0;width:1200px;text-align:center;font-size:10px;text-transform:uppercase}
.clap{display:inline-block;width:18px;height:14px;background:#fff;vertical-align:middle;margin-right:6px}
.arrow{position:absolute;width:36px;height:36px;background:var(--gold-btn);display:flex;align-items:center;justify-content:center}

/* header */
.hero{top:0;height:660px;background:radial-gradient(ellipse at 75% 60%,#3a3a3a,#111 70%)}
.logo{left:112px;top:6px;font-size:34px;color:var(--gold)}
.nav{left:365px;top:22px;display:flex;gap:52px;font-size:12px}
.phone{left:856px;top:10px;width:112px;height:34px;border:1px solid #777;font-size:11px;display:flex;align-items:center;justify-content:center;gap:6px}
.contact-top{left:976px;top:10px;width:112px;height:34px;font-size:11px}
.follow{left:112px;top:170px;font-size:11px;writing-mode:vertical-rl;transform:rotate(180deg)}
.social-dot{left:114px;width:8px;height:8px;background:var(--gold)}
.hero h1{position:absolute;left:590px;top:195px;font-family:"Cinzel",serif;font-weight:400;font-size:54px;line-height:72px;letter-spacing:2px}
.hero p{position:absolute;left:590px;top:352px;width:490px;font-size:14px;line-height:22px}

/* categories */
.categories{top:660px;height:745px;background:linear-gradient(#2a2a2a,#1d1d1d)}
.cat{position:absolute;width:313px;height:238px}
.cat .name{position:absolute;left:16px;bottom:32px;font-family:"Cinzel",serif;font-size:21px;color:var(--gold);letter-spacing:1px}
.cat .genre{position:absolute;left:16px;bottom:14px;font-size:12px}

/* about */
.about{top:1405px;height:410px;background:linear-gradient(90deg,#1a1a1a,#2d2d2d 50%,#161616)}
.block-title{position:absolute;font-family:"Cinzel",serif;font-size:30px;letter-spacing:2px}
.body-text{position:absolute;font-size:11.5px;line-height:18.5px;color:var(--muted)}

/* offer */
.offer{top:1815px;height:725px;background:linear-gradient(#232323,#1a1a1a)}

/* services */
.services{top:2540px;height:395px;background:#262626}
.svc{position:absolute;top:170px;width:220px;text-align:center}
.svc svg{display:block;margin:0 auto 6px}
.svc h3{font-family:"Cinzel",serif;font-weight:400;font-size:19px;color:var(--gold);letter-spacing:1px}
.svc p{font-size:11px;line-height:18px;margin-top:4px}

/* projects */
.projects{top:2935px;height:1010px;background:radial-gradient(ellipse at 50% 50%,#3a3a3a,#151515 75%)}
.video{position:absolute;width:488px;height:335px}
.play{position:absolute;left:50%;top:50%;width:120px;height:82px;margin:-41px 0 0 -60px;background:var(--red);opacity:.85;border-radius:18px}
.play::after{content:"";position:absolute;left:50px;top:24px;border-left:30px solid #fff;border-top:17px solid transparent;border-bottom:17px solid transparent}

/* stats */
.stats{top:3945px;height:345px;background:#161616}
.stat{position:absolute;top:215px;text-align:center;width:180px}
.stat b{display:block;font-family:"Cinzel",serif;font-weight:400;font-size:50px;line-height:56px}
.stat span{font-size:17px;text-transform:uppercase}

/* news */
.news{top:4290px;height:575px;background:linear-gradient(#262626,#1b1b1b)}
.card{position:absolute;top:150px;width:300px}
.card .img{height:182px}
.card .meta{font-size:10px;margin-top:12px;text-transform:uppercase}
.card h3{font-family:"Cinzel",serif;font-weight:400;font-size:24px;margin-top:6px;white-space:nowrap}
.card p{font-size:11px;line-height:18px;margin-top:6px}

/* newsletter */
.newsletter{top:4865px;height:171px;background:var(--gold)}
.newsletter h2{position:absolute;left:112px;top:50px;font-family:"Cinzel",serif;font-weight:400;font-size:40px;letter-spacing:1px}
.newsletter p{position:absolute;left:112px;top:100px;font-size:14px}
.email{position:absolute;left:602px;top:62px;width:338px;height:44px;background:#fff;color:#333;font-size:11px;padding:16px 38px}
.subscribe{position:absolute;left:940px;top:62px;width:150px;height:44px;background:#111;font-size:11px;display:flex;align-items:center;justify-content:center;font-weight:500}

/* footer */
.footer{top:5036px;height:236px;background:#131313}
.footer h4{position:absolute;top:40px;font-family:"Cinzel",serif;font-weight:400;font-size:20px;color:var(--gold)}
.flist{position:absolute;top:74px;font-size:11px;line-height:25px}
.sq{display:inline-block;width:12px;height:12px;background:var(--gold);vertical-align:middle;margin-right:6px}
.input{position:absolute;left:906px;width:172px;height:24px;background:#fff;color:#555;font-size:9px;padding:6px 10px}
</style>
</head>
<body>

<header class="hero">
  <div class="photo" role="img" aria-label="Black and white portrait of the filmmaker" style="left:120px;top:60px;width:470px;height:600px;background:radial-gradient(ellipse at 45% 40%,#8a8a8a,#3c3c3c 55%,transparent 75%)"></div>
  <div class="photo" role="img" aria-label="Film camera equipment in the background" style="left:760px;top:300px;width:440px;height:360px;background:radial-gradient(ellipse,#4a4a4a,transparent 70%)"></div>
  <div class="abs logo serif">LOGO</div>
  <nav class="abs nav"><span>Home</span><span>Offer</span><span>References</span><span>About me</span><span>Imprint</span></nav>
  <div class="abs phone"><svg width="10" height="10" viewBox="0 0 10 10"><path d="M2 0l2 2-1 1.5c.6 1.3 1.4 2 2.5 2.5L7 5l2 2-1.5 2C4 9 1 6 1 1.5z" fill="#fff"/></svg>123 456 7890</div>
  <div class="btn contact-top">Contact us</div>
  <div class="abs follow">Follow Us</div>
  <div class="abs" style="left:117px;top:235px;width:1px;height:30px;background:#fff"></div>
  <div class="abs social-dot" style="top:270px"></div>
  <div class="abs social-dot" style="top:300px"></div>
  <div class="abs social-dot" style="top:325px"></div>
  <h1>HEY ,<br>MY NAME IS <span class="gold">JONAS</span></h1>
  <p>My name is Jonas and I do movies - with enthusiasm and wholeheartedly. I am a holistic filmmaker.</p>
  <div class="btn" style="left:590px;top:422px;width:182px;height:56px">Contact us</div>
</header>

<section class="categories">
  <div class="ghost" style="top:-20px">HOLISTIC FILMMAKER</div>
  <div class="kicker" style="top:40px"><span class="clap"></span>Now in cinema</div>
  <div class="sec-title" style="top:68px">CATEGORIES <span class="gold">CINEMA</span></div>
  <div class="cat" role="img" aria-label="Island cliffs over a turquoise bay" style="left:112px;top:130px;background:linear-gradient(#6aa0c8,#3e6b4a 50%,#1f4f55)"><div class="name">ISLAND</div><div class="genre">Comedy</div></div>
  <div class="cat" role="img" aria-label="Friends sitting at a cafe bar" style="left:442px;top:130px;background:linear-gradient(#4a4540,#2b2622)"><div class="name">CAFE BAR</div><div class="genre">Retro</div></div>
  <div class="cat" role="img" aria-label="Woman in a red coat and hat" style="left:772px;top:130px;background:linear-gradient(#7b7a62,#8a2a2a 60%,#3a2e2a)"><div class="name">GIRLS</div><div class="genre">Comedy</div></div>
  <div class="cat" role="img" aria-label="Couple in a warm romantic scene" style="left:112px;top:386px;background:linear-gradient(#5a2a1e,#2a120c)"><div class="name">RETRO</div><div class="genre">Romance</div></div>
  <div class="cat" role="img" aria-label="Library aisle lined with bookshelves" style="left:442px;top:386px;background:linear-gradient(90deg,#7a5a38,#c4b49a 50%,#7a5a38)"><div class="name">HAPPINESS</div><div class="genre">Fiction</div></div>
  <div class="cat" role="img" aria-label="Tropical beach with turquoise water" style="left:772px;top:386px;background:linear-gradient(#6fb4dc,#2a8a6a 35%,#46c3c8 55%,#e0d6b8)"><div class="name">ACTION</div><div class="genre">Retro</div></div>
  <div class="arrow" style="left:548px;top:643px"><svg width="12" height="14"><path d="M9 1L3 7l6 6" stroke="#333" stroke-width="1.5" fill="none"/></svg></div>
  <div class="arrow" style="left:604px;top:643px"><svg width="12" height="14"><path d="M3 1l6 6-6 6" stroke="#333" stroke-width="1.5" fill="none"/></svg></div>
</section>

<section class="about">
  <div class="photo" role="img" aria-label="Black and white portrait of the filmmaker smiling" style="left:0;top:0;width:555px;height:410px;background:radial-gradient(ellipse at 45% 45%,#9a9a9a,#3a3a3a 55%,#1a1a1a)"></div>
  <div class="block-title" style="left:590px;top:55px"><span class="clap"></span>ABOUT <span class="gold">ME</span></div>
  <div class="body-text" style="left:590px;top:110px;width:500px">My name is Jonas and I do movies - with enthusiasm and wholeheartedly. I am a holistic filmmaker.<br>At the end of the 1990s, I was faced with the question of whether I should go into alternative medicine or the film industry as a career. Professionally, I chose film at that time, but the spiritual<br>and my passion for the so-called alternative healing methods have accompanied me almost as intensely ever since.<br>My cinematic path literally brought me from cable guy to cameraman, director and producer. It all</div>
  <div class="btn" style="left:590px;top:292px;width:182px;height:56px">Learn more</div>
</section>

<section class="offer">
  <div class="block-title" style="left:140px;top:110px"><span class="clap"></span>MY <span class="gold">OFFER</span></div>
  <div class="body-text" style="left:140px;top:168px;width:428px;color:#fff">Making a movie is always a journey to yourself. With simple means and without special effects, I<br>accompany you on the way to portraying your essence. A documentary commercial film close to<br>the people. Clearlight Films is aimed at all people and institutions whose striving for<br>truthfulness is the driving force behind their actions.<br>High-quality image design and the informative and comprehensible communication of complex<br>issues are the passion and basis of my image films and company presentations.<br>As a full-service provider, I offer everything from one source, from consulting and conception to<br>the finished film.<br>Advertising films, image films, company presentations, interviews, documentaries, event<br>recordings, also with several cameras or live streams - I am supported by a long-standing and<br>excellent network of freelancers, creatives and technical service providers</div>
  <div class="btn" style="left:140px;top:537px;width:182px;height:56px">Learn more</div>
  <div class="photo" role="img" aria-label="Filmmaker smiling beside a professional video camera" style="left:643px;top:67px;width:460px;height:595px;background:linear-gradient(#3f4a2e,#6a6a48 40%,#1e1e1e 80%)"></div>
</section>

<section class="services">
  <div class="ghost" style="top:-10px;left:45px">HOLISTIC FILMMAKER</div>
  <div class="kicker" style="top:65px"><span class="clap"></span></div>
  <div class="sec-title" style="top:92px">OUR <span class="gold">SERVICES</span></div>
  <div class="svc" style="left:130px"><svg width="52" height="62" viewBox="0 0 52 62" fill="none" stroke="#fff" stroke-width="2"><rect x="6" y="4" width="40" height="18"/><path d="M4 34h44M10 22l32 38M42 22L10 60"/></svg><h3>DIRECTORS</h3><p>Lorem Ipsum is simply dummy text of the printing and typesetting industry. Lorem Ipsum has been</p></div>
  <div class="svc" style="left:362px"><svg width="60" height="62" viewBox="0 0 60 62" fill="none" stroke="#fff" stroke-width="2"><path d="M22 4l8 10 8-10"/><rect x="4" y="14" width="52" height="40" rx="3"/><rect x="10" y="20" width="32" height="28"/><circle cx="49" cy="26" r="2"/><circle cx="49" cy="36" r="2"/></svg><h3>TV SHOWS</h3><p>Lorem Ipsum is simply dummy text of the printing and typesetting industry. Lorem Ipsum has been</p></div>
  <div class="svc" style="left:605px"><svg width="62" height="62" viewBox="0 0 62 62" fill="none" stroke="#fff" stroke-width="2"><circle cx="31" cy="31" r="16"/><path d="M31 6v8M26 20h10M26 42h10M31 48v8M8 20c-4 10-2 22 6 30M54 20c4 10 2 22-6 30"/></svg><h3>FILM FESTIVALS</h3><p>Lorem Ipsum is simply dummy text of the printing and typesetting industry. Lorem Ipsum has been</p></div>
  <div class="svc" style="left:850px"><svg width="44" height="64" viewBox="0 0 44 64" fill="none" stroke="#fff" stroke-width="2"><path d="M22 3l5 10 11 1-8 7 3 11-11-6-11 6 3-11-8-7 11-1z"/><path d="M22 32v16M10 48h24v12H10z"/></svg><h3>FILM AWARDS</h3><p>Lorem Ipsum is simply dummy text of the printing and typesetting industry. Lorem Ipsum has been</p></div>
</section>

<section class="projects">
  <div class="kicker" style="top:68px"><span class="clap"></span>Our works</div>
  <div class="sec-title" style="top:95px">FEATURED <span class="gold">PROJECT</span></div>
  <div class="video" role="img" aria-label="Video still: woman in a pink sweater by a whiteboard" style="left:112px;top:186px;background:linear-gradient(90deg,#d8d2c6,#b03060 55%,#6a4a3a)"><div class="play"></div></div>
  <div class="video" role="img" aria-label="Video still: people gathered outdoors on a lawn" style="left:600px;top:186px;background:linear-gradient(#3a5a2a,#7a6a50 50%,#a02a2a)"><div class="play"></div></div>
  <div class="video" role="img" aria-label="Video still: woman in front of a TV tower under blue sky" style="left:112px;top:521px;background:linear-gradient(#5a8ad0,#a8c6e8 60%,#3a2a22)"><div class="play"></div></div>
  <div class="video" role="img" aria-label="Video still: man in a suit standing by a tree" style="left:600px;top:521px;background:linear-gradient(#9aa2a8,#4a4a3a 60%,#2a2a24)"><div class="play"></div></div>
  <div class="btn" style="left:502px;top:883px;width:201px;height:54px">View all project</div>
</section>

<section class="stats">
  <div class="photo" role="img" aria-label="Black and white photo of the filmmaker behind a camera" style="left:0;top:0;width:620px;height:345px;background:radial-gradient(ellipse at 45% 50%,#8a8a8a,#2e2e2e 60%,#161616)"></div>
  <div class="kicker" style="top:60px;left:495px;width:610px"><span class="clap"></span></div>
  <div class="abs serif" style="left:590px;top:90px;width:420px;text-align:center;font-size:30px;letter-spacing:2px">NEW WAVE <span class="gold">FILMS</span></div>
  <div class="abs" style="left:590px;top:140px;width:460px;font-size:11px;line-height:19px">Lorem Ipsum is simply dummy text of the printing and typesetting industry. Lorem Ipsum has been the industry's standard dummy text ever since the 1500s, when an</div>
  <div class="stat" style="left:497px"><b>75</b><span>Years</span></div>
  <div class="stat" style="left:672px"><b>7842</b><span>Videos</span></div>
  <div class="stat" style="left:905px"><b>3250</b><span>Film Awards</span></div>
</section>

<section class="news">
  <div class="ghost" style="top:-5px">HOLISTIC FILMMAKER</div>
  <div class="kicker" style="top:60px"><span class="clap"></span></div>
  <div class="sec-title" style="top:88px">LESTES <span class="gold">NEWS</span></div>
  <div class="card" style="left:137px"><div class="img" role="img" aria-label="Film set with lights and director's chair" style="background:linear-gradient(#e0e0e0,#6a6a6a 55%,#2a2a2a)"></div><div class="meta">April 20, 2018 by Lena Hart Actors</div><h3>AWARD CEREMONY</h3><p>Lorem Ipsum is simply dummy text of the printing and typesetting industry. Lorem Ipsum has been the industry's standard dummy text ever since the 1500s,</p></div>
  <div class="card" style="left:452px"><div class="img" role="img" aria-label="Camera crew filming on location" style="background:linear-gradient(#6a5a48,#3a2e26)"></div><div class="meta">April 20, 2018 by Lena Hart Actors</div><h3>HEROES FOR A DAY</h3><p>Lorem Ipsum is simply dummy text of the printing and typesetting industry. Lorem Ipsum has been the industry's standard dummy text ever since the 1500s,</p></div>
  <div class="card" style="left:768px"><div class="img" role="img" aria-label="Close-up of a cinema camera lens" style="background:radial-gradient(ellipse at 45% 60%,#3a3a3a,#0e0e0e 70%)"></div><div class="meta">April 20, 2018 by Lena Hart Actors</div><h3>OUTDOOR SHOOTING</h3><p>Lorem Ipsum is simply dummy text of the printing and typesetting industry. Lorem Ipsum has been the industry's standard dummy text ever since the 1500s,</p></div>
  <div class="arrow" style="left:552px;top:480px"><svg width="12" height="14"><path d="M9 1L3 7l6 6" stroke="#333" stroke-width="1.5" fill="none"/></svg></div>
  <div class="arrow" style="left:610px;top:480px"><svg width="12" height="14"><path d="M3 1l6 6-6 6" stroke="#333" stroke-width="1.5" fill="none"/></svg></div>
</section>

<section class="newsletter">
  <h2>NEWSLETTER SIGN UP</h2>
  <p>Subscribe for news, updates, and promotions.</p>
  <div class="email">Enter Your Email</div>
  <div class="subscribe">SUBSCRIBE</div>
</section>

<footer class="footer">
  <div class="abs serif gold" style="left:112px;top:36px;font-size:26px">LOGO</div>
  <div class="abs" style="left:112px;top:78px;width:220px;font-size:10px;line-height:18px">Lorem Ipsum is simply dummy text of the printing and typesetting industry. Lorem Ipsum has been the industry's standard dummy text ever since the 1500s, when an</div>
  <div class="abs" style="left:112px;top:208px;font-size:10px">Copyright © 2010-2023 Jonas.com</div>
  <h4 style="left:434px">ABOUT US</h4>
  <div class="flist" style="left:434px;top:68px">Home<br>Offer<br>References<br>About me<br>Imprint</div>
  <h4 style="left:662px">FOLLOW US</h4>
  <div class="flist" style="left:662px"><span class="sq"></span>Lumenet<br><span class="sq"></span>Echoline<br><span class="sq"></span>Framely</div>
  <h4 style="left:906px">CONTACT US</h4>
  <div class="input" style="top:72px">Name</div>
  <div class="input" style="top:106px">Address</div>
  <div class="btn" style="left:906px;top:142px;width:86px;height:28px;font-size:10px">Submit</div>
</footer>

</body>
</html>
```